Voucher design for Willow Brook Spa

1) Create a creative design and voucher for Willow Brook Spa that create a lasting memory for the audience. I would like to give out vouchers to all neighbours.
2) Kindly look at the website www.willowbrookspa-example.net
3) Content must include logo, address, telephone number and website.

Here is the content of the voucher

2) 15 dollar cash voucher - off full body massage
3) 10 dollars cash voucher - off foot massage
(Both the fully body massage and foot massage, slimming massage vouchers must be separated and separate vouchers and independent)
4) 20 dollars cash voucher - off slimming massage

Terms and conditions at the back of the voucher
1) Willow Brook Spa reserved the right to amend change the terms and conditions without prior notice.
2) This promotional is not valid with any other promotions existing. e.g
3) Each person is entitled to use one voucher at any one time.

Target Market(s)

Mass market

Font styles to use
Decorative

Requirements
Must have
• 1) Creatives cash vouchers and beautiful design
• 2) Logo fo the company
• 3) Address and telephone number
• 4) website
• 5) Terms and conditions
Nice to have
• You can use tree or lotus as the symbol but it must be toward nature, beautiful, eye catching and creative.

```html
<!DOCTYPE html>
<html lang="en">
<head>
<meta charset="utf-8">
<title>Willow Brook Spa – Cash Vouchers</title>
<link href="https://fonts.googleapis.com/css2?family=Bebas+Neue&family=Lato:ital,wght@0,400;0,700;1,400&family=Open+Sans:wght@400;600&display=swap" rel="stylesheet">
<style>
  :root{
    --green:#7ed321;
    --green-light:#9be83a;
    --green-dark:#5fae12;
    --ink:#1c1c1c;
    --bar:#25272a;
    --panel:#eef0f1;
    --orange:#f7941d;
    --orange-light:#ffc24a;
    --brand:#3a8fc9;
    --page:#e9eaeb;
    --white:#ffffff;
  }
  *{margin:0;padding:0;box-sizing:border-box}
  html,body{width:1200px;height:1200px;overflow:hidden;background:var(--page)}
  .voucher{position:absolute;left:291px;width:638px;height:495px;background:var(--white);overflow:hidden}
  .voucher--front{top:90px}
  .voucher--back{top:648px}
  .voucher__art{position:absolute;inset:0;width:100%;height:100%}
  .title{position:absolute;right:28px;text-align:right;color:var(--white)}
  .title__name{font-family:"Bebas Neue",sans-serif;font-size:50px;line-height:1;letter-spacing:0.5px}
  .title__tag{font-family:"Lato",sans-serif;font-style:italic;font-size:25px;line-height:1.1;margin-top:2px}
  .voucher--front .title{top:62px}
  .voucher--back .title{top:32px}
  .join{position:absolute;width:128px;height:128px;border-radius:50%;
    background:radial-gradient(circle at 50% 35%,var(--orange-light) 0%,var(--orange) 55%,#e8760c 100%);
    border:5px solid var(--white);box-shadow:0 6px 10px rgba(0,0,0,.18);
    display:flex;align-items:center;justify-content:center;text-align:center;
    font-family:"Bebas Neue",sans-serif;color:var(--white);font-size:46px;line-height:0.9}
  .voucher--front .join{left:37px;top:210px}
  .voucher--back .join{left:481px;top:328px}
  .offers{position:absolute;left:230px;top:232px;width:400px;display:flex}
  .offer{flex:1;text-align:center;font-family:"Bebas Neue",sans-serif;line-height:0.95}
  .offer__price{font-size:72px;color:var(--ink)}
  .offer__kind{font-size:30px;color:var(--green-dark)}
  .offer__kind--big{font-size:44px}
  .offer__type{font-size:32px;color:var(--ink)}
  .brand{position:absolute;display:flex;align-items:center;gap:6px;font-family:"Lato",sans-serif;font-weight:700;font-size:15px;color:var(--brand);white-space:nowrap}
  .brand__dot{width:12px;height:12px;border-radius:50%;background:var(--green)}
  .voucher--front .brand{left:30px;top:402px}
  .voucher--back .brand{left:468px;top:252px}
  .web{position:absolute;right:26px;top:446px;font-family:"Open Sans",sans-serif;font-size:13px;letter-spacing:1.5px;color:var(--ink);white-space:nowrap}
  .bar{position:absolute;left:0;bottom:0;width:100%;height:15px;background:var(--bar)}
  .terms__label{position:absolute;left:0;top:323px;width:201px;height:28px;border-radius:0 14px 14px 0;background:var(--green);
    color:var(--white);font-family:"Open Sans",sans-serif;font-weight:600;font-size:15px;line-height:28px;padding-left:26px}
  .terms__list{position:absolute;left:28px;top:384px;width:450px;list-style:none;font-family:"Open Sans",sans-serif;font-size:13px;line-height:18px;color:var(--ink)}
  .terms__list li{position:relative;padding-left:18px;margin-bottom:8px;white-space:nowrap}
  .terms__list li::before{content:"";position:absolute;left:0;top:5px;width:9px;height:9px;border-radius:50%;background:var(--green)}
</style>
</head>
<body>

<section class="voucher voucher--front">
  <svg class="voucher__art" viewBox="0 0 638 495" preserveAspectRatio="none">
    <defs>
      <linearGradient id="frontHeader" x1="0" y1="0" x2="1" y2="0">
        <stop offset="0" stop-color="#86de25"/><stop offset="1" stop-color="#9be83a"/>
      </linearGradient>
      <linearGradient id="frontPanel" x1="0" y1="0" x2="0" y2="1">
        <stop offset="0" stop-color="#e4e7e8"/><stop offset="1" stop-color="#ffffff"/>
      </linearGradient>
      <linearGradient id="massagePhoto" x1="0" y1="0" x2="1" y2="1">
        <stop offset="0" stop-color="#f6e6c9"/><stop offset=".55" stop-color="#e2b08f"/><stop offset="1" stop-color="#f4ece1"/>
      </linearGradient>
    </defs>
    <rect x="290" y="197" width="348" height="200" fill="url(#frontPanel)"/>
    <path d="M300 0 H638 V190 H270 C300 130 318 70 322 0 Z" fill="url(#frontHeader)"/>
    <path role="img" aria-label="Photo of a woman relaxing during a hot stone back massage" d="M0 0 H312 C300 110 250 180 150 215 L0 225 Z" fill="url(#massagePhoto)"/>
    <path d="M316 0 C304 115 250 188 150 222" fill="none" stroke="var(--white)" stroke-width="6"/>
    <path d="M326 0 C316 120 262 196 158 232" fill="none" stroke="var(--green)" stroke-width="7"/>
    <rect x="290" y="190" width="348" height="6" fill="var(--bar)"/>
    <path d="M22 420 C30 350 70 300 135 280" fill="none" stroke="var(--green)" stroke-width="3"/>
    <path d="M165 332 C188 420 232 468 282 495" fill="none" stroke="var(--green)" stroke-width="4"/>
    <path d="M262 495 C292 440 340 410 440 404 C560 398 612 388 638 362 L638 374 C612 400 560 410 440 416 C350 420 305 450 276 495 Z" fill="var(--green)"/>
  </svg>
  <div class="title">
    <div class="title__name">Willow Brook Spa</div>
    <div class="title__tag">Meditation &amp; message</div>
  </div>
  <div class="join">JOIN<br>US!</div>
  <div class="offers">
    <div class="offer"><div class="offer__price">$15</div><div class="offer__kind">Full Body</div><div class="offer__type">Massage</div></div>
    <div class="offer"><div class="offer__price">$10</div><div class="offer__kind offer__kind--big">Foot</div><div class="offer__type">Massage</div></div>
    <div class="offer"><div class="offer__price">$20</div><div class="offer__kind">Slimming</div><div class="offer__type">Massage</div></div>
  </div>
  <div class="brand"><span class="brand__dot"></span>Willow Brook Spa</div>
  <div class="web">www.willowbrookspa-example.net</div>
  <div class="bar"></div>
</section>

<section class="voucher voucher--back">
  <svg class="voucher__art" viewBox="0 0 638 495" preserveAspectRatio="none">
    <defs>
      <linearGradient id="backHeader" x1="0" y1="0" x2="1" y2="0">
        <stop offset="0" stop-color="#86de25"/><stop offset="1" stop-color="#9be83a"/>
      </linearGradient>
      <linearGradient id="backPanel" x1="0" y1="0" x2="0" y2="1">
        <stop offset="0" stop-color="#ffffff"/><stop offset="1" stop-color="#eceeef"/>
      </linearGradient>
      <linearGradient id="portraitPhoto" x1="0" y1="0" x2="0" y2="1">
        <stop offset="0" stop-color="#f3e7df"/><stop offset=".5" stop-color="#ecc9b4"/><stop offset="1" stop-color="#f6ece6"/>
      </linearGradient>
      <linearGradient id="spaItems" x1="0" y1="0" x2="1" y2="0">
        <stop offset="0" stop-color="#f6c27a"/><stop offset=".5" stop-color="#f2e6cf"/><stop offset="1" stop-color="#d9d9d4"/>
      </linearGradient>
    </defs>
    <rect x="0" y="290" width="638" height="190" fill="url(#backPanel)"/>
    <path d="M110 0 H638 V170 H340 C280 120 220 40 110 0 Z" fill="url(#backHeader)"/>
    <rect x="340" y="170" width="298" height="6" fill="var(--bar)"/>
    <path d="M85 0 C200 50 290 170 380 260 C430 310 470 340 520 360" fill="none" stroke="var(--green)" stroke-width="6"/>
    <path role="img" aria-label="Portrait photo of a woman with smooth skin, hands framing her face" d="M40 20 H290 C300 120 320 220 330 290 L35 290 Z" fill="url(#portraitPhoto)"/>
    <path d="M0 300 C120 270 300 270 420 310 C480 330 520 350 540 370 L536 378 C500 352 440 330 400 320 C290 292 130 292 0 318 Z" fill="var(--green)"/>
    <path d="M600 370 C615 365 628 360 638 355" fill="none" stroke="var(--green)" stroke-width="5"/>
    <rect role="img" aria-label="Photo of candles, a honey jar, daisies and black massage stones" x="221" y="285" width="143" height="83" rx="30" fill="url(#spaItems)"/>
  </svg>
  <div class="title">
    <div class="title__name">Willow Brook Spa</div>
    <div class="title__tag">Meditation &amp; message</div>
  </div>
  <div class="brand"><span class="brand__dot"></span>Willow Brook Spa</div>
  <div class="terms__label">Terms and conditions</div>
  <ul class="terms__list">
    <li>Willow Brook Spa reserved the right to amend<br>change the terms and conditions withoutprior notice.</li>
    <li>This promotional is not valid with any other promotions existing. e.g<br>Each person is entitled to use one voucher at any one time.</li>
  </ul>
  <div class="join">JOIN<br>US!</div>
  <div class="bar"></div>
</section>

</body>
</html>
```